Varnock Travel letterhead design

We need a design for a simple document where we can dump our own information within it. A simple letterhead style. No address or phone details etc are required. More just our logo and free format. Hope this makes sense !

```html
<!DOCTYPE html>
<html lang="en">
<head>
<meta charset="utf-8">
<title>Varnock Travel Letterhead</title>
<link rel="stylesheet" href="https://fonts.googleapis.com/css2?family=Montserrat:wght@400;700;800&display=swap">
<style>
  :root {
    --backdrop: #a5a6aa;
    --paper: #ffffff;
    --brand-blue: #17487a;
    --ink: #111111;
    --watermark: #c9cbdc;
    --signature-tone: #d4d4d6;
  }
  * { box-sizing: border-box; margin: 0; padding: 0; }
  html, body {
    width: 1000px;
    height: 1200px;
    overflow: hidden;
    background: var(--backdrop);
    font-family: "Montserrat", Arial, sans-serif;
  }
  .letterhead {
    position: absolute;
    left: 113px;
    top: 75px;
    width: 782px;
    height: 1010px;
    background: var(--paper);
    overflow: hidden;
  }
  .header-bar {
    position: absolute;
    top: 42px;
    height: 81px;
    background: var(--brand-blue);
  }
  .header-bar--left { left: 0; width: 24px; }
  .header-bar--right { left: 368px; width: 414px; }
  .brand-name {
    position: absolute;
    left: 39px;
    top: 42px;
    height: 81px;
    line-height: 81px;
    font-size: 40px;
    font-weight: 800;
    letter-spacing: -1px;
    color: var(--brand-blue);
    white-space: nowrap;
  }
  .watermark {
    position: absolute;
    left: 0;
    width: 782px;
    top: 410px;
    text-align: center;
    font-size: 120px;
    font-weight: 800;
    letter-spacing: -3px;
    line-height: 1;
    color: var(--watermark);
    white-space: nowrap;
  }
  .letter-body {
    position: absolute;
    left: 87px;
    top: 248px;
    width: 608px;
    font-size: 15px;
    line-height: 27px;
    color: var(--ink);
  }
  .salutation { font-weight: 700; margin-bottom: 52px; }
  .letter-body p.paragraph {
    text-align: justify;
    hyphens: auto;
    margin-bottom: 27px;
  }
  .sign-off {
    position: absolute;
    left: 556px;
    top: 762px;
    width: 100px;
    text-align: center;
    font-size: 15px;
    font-weight: 700;
    color: var(--ink);
  }
  .signature {
    display: block;
    width: 62px;
    height: 66px;
    margin: 6px auto 0;
    background: var(--signature-tone);
  }
  .signer-name { display: block; margin-top: 2px; }
</style>
</head>
<body>
  <main class="letterhead">
    <header>
      <div class="header-bar header-bar--left"></div>
      <div class="brand-name">Varnock Travel</div>
      <div class="header-bar header-bar--right"></div>
    </header>

    <div class="watermark" aria-hidden="true">Varnock</div>

    <section class="letter-body" lang="la">
      <p class="salutation">Dear Client Name,</p>
      <p class="paragraph">Lorem ipsum dolor sit amet, consectetur adipiscing elit. Praesent sed interdum ipsum. Ut tincidunt mauris quis sodales blandit. Sed nunc quam, sollicitudin vel arcu vel, tincidunt viverra nisl. Nullam ut sagittis nisi. Pellentesque mauris purus, mollis ut vehicula at, consequat sit amet lacus. Vestibulum nec cursus ligula. Aliquam erat volutpat.</p>
      <p class="paragraph">Donec consequat, diam ac tristique bibendum, neque magna consequat mauris, ac condimentum sapien tortor egestas nibh. Aliquam hendrerit pretium enim id suscipit. Curabitur ut urna ultricies, laoreet lacus quis, congue odio. Proin risus erat, vestibulum sit amet mauris vitae, ultricies ornare tortor. Maecenas eget nulla ipsum. Vestibulum a vulputate turpis. Sed et lobortis nibh. Cras at maximus orci. Ut lectus libero, dignissim vulputate justo ut, semper blandit ex.</p>
    </section>

    <footer class="sign-off">
      <span>Regards,</span>
      <span class="signature" role="img" aria-label="Handwritten signature of the sender"></span>
      <span class="signer-name">JOHN DOE</span>
    </footer>
  </main>
</body>
</html>
```